Home Page Design for Motor Manufacturer

Hello,
please design the homepage for a manufacturer of industry motors. I am looking for a professional, clean and minimalistic design. Since this a rather conservative industry it should get a professional look but since it is a redesign there should be some modern that gives is the modern touch of innovation.
A competitor's homepage I like is:
https://www.valtrosk.com/en/
What I like about this website:
* clean, minimal, well structured design
* mega menu
For this project please find attached the wireframes (most buttons are in German but by context and Google translate you will easily figure it out; only unclear - "Messe" means "trade exhibition"). The paddings and margins are NOT exact. Also any color of backgrounds etc. chosen is not meant to represent a real color but rather to illustrate the object and maybe show there should be some background emphasis (color or image).
Wireframes:
https: //www.filmavek. com / t / pxuTQmD7ZJHaLrwY
In both wireframes the only thing that is different is the Service section. I expect from the winner both designs for this service section: one with normal cart design and one with tabs as filters to search products (find image for product categories attached)
In the header use on the left the following text:
h1: "Your competent partner for industrial engines,
-transmission and drawing parts
with more than 5000 satisfied customers "
primary button: Our products
sec. button: Download catalog
and on the right side we feature one or more product images (like putting them in a nice display together).
I also think of a solid background color or subtle gradient for the hero section.
The winner should also design an open mega menu version.
Menu items in this order:
• Home page
• Gearboxes & Motors
• Engine components
• Drawing parts
• Machines & accessories
• About us
• Contact
Also create a language switch with globe symbol and DE for Germany and EN for English above the nav plus the telephone number with icon (user dummy number +49 (0) 987654321)
Output should be in Figma, Sketch or PSD.
Fonts + color to use:
header: Proza Libre, bold, # 0171A1
body: Open Sans, regular, black
Primary accent color: # 0171A1
Text black or dark gray
background: light gray, white or shade of blue
More image resources:
https://www.filmavek.com/t/QrnLVdHZPKEX1bmu
If there are any questions please do not hesitate to ask.
Target Market(s)
B2B - anyone with industrial machinery needing small motors (not car engines)
Industry/Entity Type
Manufacturing
Number of Pages Required
1 page
Requirements
Must have
- see above
Nice to have
- see above
Should not have
- see above

```html
<!DOCTYPE html>
<html lang="en">
<head>
<meta charset="utf-8">
<title>Morvida – Industrial engines, transmission and drawing parts</title>
<link rel="stylesheet" href="https://fonts.googleapis.com/css2?family=Open+Sans:wght@400;600&family=Proza+Libre:wght@500;600;700&display=swap">
<style>
  :root {
    --accent: #0171a1;
    --text: #111111;
    --nav-text: #2b2b2b;
    --muted: #707070;
    --bg-top: #eff7f4;
    --bg-bottom: #e3f3f8;
    --metal-light: #eef0f1;
    --metal-mid: #d3d8db;
    --metal-dark: #b4bcc1;
  }
  * { box-sizing: border-box; margin: 0; padding: 0; }
  html, body { width: 1200px; height: 853px; overflow: hidden; }
  body {
    font-family: "Open Sans", sans-serif;
    color: var(--text);
    background: linear-gradient(170deg, var(--bg-top) 0%, var(--bg-top) 55%, var(--bg-bottom) 100%);
    position: relative;
  }
  .hero-visual {
    position: absolute;
    left: 588px; top: 121px;
    width: 612px; height: 732px;
  }
  .site-header { position: absolute; inset: 0 0 auto 0; height: 120px; z-index: 2; }
  .brand {
    position: absolute; left: 118px; top: 76px;
    font-family: "Proza Libre", sans-serif;
    font-weight: 700; font-size: 28px; color: var(--accent);
    display: flex; align-items: center; gap: 8px;
  }
  .brand-dot { width: 14px; height: 14px; border-radius: 50%; background: var(--accent); }
  .lang-switch {
    position: absolute; left: 268px; top: 50px;
    display: flex; align-items: center; gap: 3px;
    font-size: 12px; color: var(--muted);
  }
  .phone {
    position: absolute; right: 119px; top: 52px;
    display: flex; align-items: center; gap: 4px;
    font-size: 11.5px; font-weight: 600; color: var(--muted);
  }
  .main-nav {
    position: absolute; left: 267px; top: 76px;
    display: flex; gap: 18px;
    font-size: 15px; color: var(--nav-text);
  }
  .main-nav a { color: inherit; text-decoration: none; position: relative; padding-bottom: 8px; }
  .main-nav a.is-active::after {
    content: ""; position: absolute; left: -4px; right: -4px; bottom: 0;
    height: 2px; background: var(--accent);
  }
  .hero-copy { position: absolute; left: 117px; top: 278px; z-index: 2; }
  .hero-title {
    font-family: "Proza Libre", sans-serif; font-weight: 700;
    font-size: 41px; line-height: 54px; color: var(--accent);
    letter-spacing: 0.2px;
  }
  .hero-sub { margin-top: 28px; margin-left: 2px; font-size: 19.5px; }
  .hero-sub strong {
    font-family: "Proza Libre", sans-serif; font-weight: 600; color: var(--accent);
  }
  .hero-actions { margin-top: 28px; margin-left: 1px; display: flex; gap: 42px; }
  .btn {
    height: 50px; display: flex; align-items: center; justify-content: center;
    font-family: "Proza Libre", sans-serif; font-weight: 600; font-size: 16px;
    text-decoration: none;
  }
  .btn-primary { width: 243px; background: var(--accent); color: #fff; }
  .btn-secondary { width: 124px; border: 2px solid var(--accent); color: var(--accent); }
</style>
</head>
<body>
  <svg class="hero-visual" role="img" aria-label="Product photo: precision planetary gearbox with gears and bearing" viewBox="0 0 612 732">
    <defs>
      <radialGradient id="metal" cx="0.55" cy="0.5" r="0.6">
        <stop offset="0" stop-color="var(--metal-light)"/>
        <stop offset="0.7" stop-color="var(--metal-mid)"/>
        <stop offset="1" stop-color="var(--metal-dark)"/>
      </radialGradient>
    </defs>
    <circle cx="420" cy="450" r="412" fill="url(#metal)"/>
  </svg>

  <header class="site-header">
    <div class="brand"><span class="brand-dot"></span>Morvida</div>
    <div class="lang-switch">
      <svg width="16" height="16" viewBox="0 0 16 16" aria-hidden="true">
        <circle cx="8" cy="8" r="7" fill="none" stroke="#888" stroke-width="1.4"/>
        <path d="M1 8h14M8 1c-3 3-3 11 0 14M8 1c3 3 3 11 0 14" fill="none" stroke="#888" stroke-width="1.2"/>
      </svg>
      <span>EN</span>
      <svg width="9" height="6" viewBox="0 0 9 6" aria-hidden="true"><path d="M1 1.5l3.5 3 3.5-3" fill="none" stroke="#888" stroke-width="1.2"/></svg>
    </div>
    <div class="phone">
      <svg width="15" height="15" viewBox="0 0 24 24" aria-hidden="true">
        <path fill="#777" d="M6.6 10.8a15 15 0 0 0 6.6 6.6l2.2-2.2a1 1 0 0 1 1-.25 11.4 11.4 0 0 0 3.6.57 1 1 0 0 1 1 1V20a1 1 0 0 1-1 1A17 17 0 0 1 3 4a1 1 0 0 1 1-1h3.5a1 1 0 0 1 1 1c0 1.25.2 2.46.57 3.6a1 1 0 0 1-.25 1z"/>
      </svg>
      <span>+49 (0) 987654321</span>
    </div>
    <nav class="main-nav">
      <a href="#" class="is-active">Home</a>
      <a href="#">Gearboxes &amp; Motors</a>
      <a href="#">Engine components</a>
      <a href="#">Drawing parts</a>
      <a href="#">Machines &amp; accessories</a>
      <a href="#">About</a>
      <a href="#">Contact</a>
    </nav>
  </header>

  <main class="hero-copy">
    <h1 class="hero-title">Your competent partner<br>for industrial engines,<br>transmission and<br>drawing parts</h1>
    <p class="hero-sub">with more than <strong>5000 satisfied customers</strong></p>
    <div class="hero-actions">
      <a href="#" class="btn btn-primary">Our products</a>
      <a href="#" class="btn btn-secondary">Get catalog</a>
    </div>
  </main>
</body>
</html>
```